LumaDerm business cards

We want to create two sets of cards. One general card for lumaderm [staff] and one card for the founder of the company. Below is the general/basic information for you to format/display on side of the cards:
--Company address: 418 Harlow Street, New York, NY 10027
--Main phone: 212-637-1582
Will also provide you with secondary 1-800 number
--company website: www.lumaderm-example.com
--email address for general card: concierge@lumaderm-example.com
--email address (for dr whitfield's card: dr@lumaderm-example.com
--titles for dr whitfield's card: Founder, Medical Director
--Dr. Whitfield's name on the card should read: Gregory T. Whitfield, MD
You can also play around with lumaderm's tag line: Radiance Kept Quietly Yours (TM or R should be attached as a trademark has been filed)
Reason: More time to design something awesome. This company is an aesthetic medical company that offers cool and safe cosmetic treatments
For the business card design for the doctor, please change the doctor's name to look like this above his title: Gregory T. Whitfield, MD instead of using Dr. Gregory....etc
Reason: WILL NOT BE ABLE TO VIEW AND FINALIZE DESIGNS UNTIL I RETURN FROM MEDICAL CONFERENCE, WHICH WILL BE ON SUNDAY/MONDAY. MY APOLOGIES
can everyone try making it very minimalistic
A Bit of a change...
Can everyone take a stab at using a grey "raw" or eco friendly stock paper. We are interested to see the designs you come up with.
Business

```html
<!DOCTYPE html>
<html lang="en">
<head>
<meta charset="utf-8">
<title>LumaDerm business cards</title>
<link rel="stylesheet" href="https://fonts.googleapis.com/css2?family=Arimo:wght@400;700&family=Libre+Baskerville:wght@400;700&display=swap">
<style>
  :root {
    --frame: #3b3b3b;
    --sheet: #ffffff;
    --card-edge: #1e1e1e;
    --spa-blue: #3bb5f6;
    --logo-blue: #45b0f0;
    --name-blue: #3d6fe6;
    --ink: #1a1a1a;
    --white: #ffffff;
    --serif: "Libre Baskerville", Georgia, serif;
    --sans: "Arimo", Arial, sans-serif;
  }
  * { box-sizing: border-box; margin: 0; padding: 0; }
  html, body { width: 942px; height: 1200px; overflow: hidden; background: var(--frame); }
  .sheet {
    position: absolute; left: 12px; top: 12px; width: 917px; height: 1177px;
    background: var(--sheet);
  }
  .set-divider {
    position: absolute; left: 23px; top: 582px; width: 871px; height: 12px;
    background: var(--frame);
  }
  .card {
    position: absolute; width: 388px; height: 221px;
    border: 1px solid var(--card-edge); background: var(--white);
    overflow: hidden;
  }
  .col-left { left: 46px; }
  .col-right { left: 481px; }
  .row-1 { top: 46px; }
  .row-2 { top: 314px; }
  .row-3 { top: 639px; }
  .row-4 { top: 908px; }

  .card__panel {
    position: absolute; left: 16px; top: 15px; right: 17px; bottom: 15px;
    background: var(--spa-blue); overflow: hidden;
  }
  .wordmark {
    position: absolute; font-family: var(--sans); font-weight: 400;
    letter-spacing: -0.5px; line-height: 1; white-space: nowrap;
  }
  .wordmark--reverse { color: var(--white); font-size: 24px; left: 20px; top: 77px; }
  .wordmark__dot {
    display: inline-block; width: 4px; height: 4px; border-radius: 50%;
    background: currentColor; vertical-align: top; margin-left: 2px; margin-top: 2px;
  }
  .rule {
    position: absolute; width: 0; border-left: 1px dotted currentColor;
  }
  .card__panel .rule { color: var(--white); left: 146px; top: 42px; height: 108px; }
  .details {
    position: absolute; left: 158px; top: 52px; color: var(--white);
    font-size: 10px; line-height: 14px; white-space: nowrap;
  }
  .details.with-email { top: 44px; }
  .details p + p { margin-top: 7px; }
  .details--serif { font-family: var(--serif); font-weight: 700; }
  .details--sans { font-family: var(--sans); font-weight: 400; font-size: 11px; letter-spacing: 0.2px; }
  .details .email { font-size: 9px; }
  .details--sans .email { font-size: 10.5px; }

  .lockup { position: absolute; color: var(--logo-blue); }
  .lockup--small { left: 16px; top: 90px; }
  .lockup--small .wordmark { position: static; font-size: 30px; }
  .lockup--large { left: 0; right: 0; top: 58px; text-align: center; }
  .lockup--large .wordmark { position: static; display: inline-block; font-size: 64px; }
  .lockup--large .wordmark__dot { width: 7px; height: 7px; margin-top: 4px; }
  .tagline {
    font-family: var(--sans); font-size: 5.5px; letter-spacing: 1.3px;
    text-transform: uppercase; margin-top: 4px; white-space: nowrap;
  }
  .lockup--large .tagline { font-size: 8.5px; letter-spacing: 2.4px; margin-top: 6px; text-align: left; padding-left: 48px; }

  .card .rule.on-white { color: var(--ink); left: 186px; top: 62px; height: 90px; }
  .founder { position: absolute; left: 200px; top: 79px; white-space: nowrap; }
  .founder__name {
    font-family: var(--serif); font-weight: 700; font-size: 10px; color: var(--name-blue);
  }
  .founder__title {
    font-family: var(--sans); font-size: 7.5px; color: var(--ink); margin-top: 3px;
  }
  .founder__email {
    font-family: var(--serif); font-size: 10px; color: var(--ink); margin-top: 10px;
  }
</style>
</head>
<body>
<main class="sheet">

  <!-- Set one: serif details -->
  <section class="card col-left row-1">
    <div class="card__panel">
      <div class="wordmark wordmark--reverse">lumaderm<span class="wordmark__dot"></span></div>
      <div class="rule"></div>
      <div class="details details--serif">
        <p>418 Harlow Street<br>New York, NY 10027</p>
        <p>212.637.1582<br>1.800.000.0000</p>
        <p>www.lumaderm-example.com</p>
      </div>
    </div>
  </section>

  <section class="card col-right row-1">
    <div class="card__panel">
      <div class="wordmark wordmark--reverse">lumaderm<span class="wordmark__dot"></span></div>
      <div class="rule"></div>
      <div class="details details--serif with-email">
        <p>418 Harlow Street<br>New York, NY 10027</p>
        <p>212.637.1582<br>1.800.000.0000</p>
        <p>www.lumaderm-example.com<br><span class="email">concierge@lumaderm-example.com</span></p>
      </div>
    </div>
  </section>

  <section class="card col-left row-2">
    <div class="lockup lockup--small">
      <div class="wordmark">lumaderm<span class="wordmark__dot"></span></div>
      <div class="tagline">Radiance Kept Quietly Yours™</div>
    </div>
    <div class="rule on-white"></div>
    <div class="founder">
      <p class="founder__name">Gregory T. Whitfield, MD</p>
      <p class="founder__title">FOUNDER, MEDICAL DIRECTOR</p>
      <p class="founder__email">dr@lumaderm-example.com</p>
    </div>
  </section>

  <section class="card col-right row-2">
    <div class="lockup lockup--large">
      <div class="wordmark">lumaderm<span class="wordmark__dot"></span></div>
      <div class="tagline">Radiance Kept Quietly Yours™</div>
    </div>
  </section>

  <div class="set-divider"></div>

  <!-- Set two: sans details -->
  <section class="card col-left row-3">
    <div class="card__panel">
      <div class="wordmark wordmark--reverse">lumaderm<span class="wordmark__dot"></span></div>
      <div class="rule"></div>
      <div class="details details--sans">
        <p>418 Harlow Street<br>New York, NY 10027</p>
        <p>212.637.1582<br>1.800.000.0000</p>
        <p>www.lumaderm-example.com</p>
      </div>
    </div>
  </section>

  <section class="card col-right row-3">
    <div class="card__panel">
      <div class="wordmark wordmark--reverse">lumaderm<span class="wordmark__dot"></span></div>
      <div class="rule"></div>
      <div class="details details--sans with-email">
        <p>418 Harlow Street<br>New York, NY 10027</p>
        <p>212.637.1582<br>1.800.000.0000</p>
        <p>www.lumaderm-example.com<br><span class="email">concierge@lumaderm-example.com</span></p>
      </div>
    </div>
  </section>

  <section class="card col-left row-4">
    <div class="lockup lockup--small">
      <div class="wordmark">lumaderm<span class="wordmark__dot"></span></div>
      <div class="tagline">Radiance Kept Quietly Yours™</div>
    </div>
    <div class="rule on-white"></div>
    <div class="founder">
      <p class="founder__name">Gregory T. Whitfield, MD</p>
      <p class="founder__title">FOUNDER, MEDICAL DIRECTOR</p>
      <p class="founder__email">dr@lumaderm-example.com</p>
    </div>
  </section>

  <section class="card col-right row-4">
    <div class="lockup lockup--large">
      <div class="wordmark">lumaderm<span class="wordmark__dot"></span></div>
      <div class="tagline">Radiance Kept Quietly Yours™</div>
    </div>
  </section>

</main>
</body>
</html>
```